Global Expert Network Firm needs business card design

We need business card design for a new company based in Seoul, South Korea called 'Corwell Insight Partners'. We recruit industry experts covering all countries and connect our client and recruited expert by phone, face-to-face meetings and etc. We are a global expert network firm that is focused on delivering high-quality experts to our clients throughout the world. Our clients include multinational corporations, global consulting firms, private equity firms, venture capital firms, asset management companies.
We have made new logo and please find attachment.(Please use new logo)
Target Market(s)
Global Consulting Firms, Investment Firms, Private Equity Firms, Venture Capital Firms.
Industry/Entity Type
Recruitment
Contact Information for Business Card
We need two Languages (English and Korean Version).
The front is Korean and the back is English version.
[The back] [English]
Company Name: Corwell Insight Partners, Inc.
CEO Name: Daniel Park
Address: #507, Hanbit Bldg, 82 Maebongsan-ro, Dobong-gu, Seoul, 01327, Korea
Tel. +82 2 718 4052
Fax. +82 2 864 1097
Mobile. +82 10 7264 8815
Email: daniel@corwellip.com
Web: www.corwellip.com
[The front] [Korean] => Described in same order as English version.
회사명: 코웰인사이트파트너스(주)
대표이사: 박도현
주소: 서울시 도봉구 매봉산로 82 한빛빌딩 507호
Tel. 02 718 4052
Fax. 02 864 1097
Mobile. 010 7264 8815
Web: www.corwellip.com
Look and feel
Each slider illustrates characteristics of the customer's brand and the style your logo design should communicate.

```html
<!DOCTYPE html>
<html lang="ko">
<head>
<meta charset="utf-8">
<title>Corwell Insight Partners — Business Cards</title>
<link rel="stylesheet" href="https://fonts.googleapis.com/css2?family=Noto+Sans+KR:wght@300;400;500&family=Nanum+Myeongjo&display=swap">
<style>
  :root {
    --navy: #1b2257;
    --paper: #f4f4f6;
    --backdrop: #2a2b2e;
    --white: #ffffff;
  }
  * { margin: 0; padding: 0; box-sizing: border-box; }
  html, body { width: 1200px; height: 1000px; overflow: hidden; }
  body {
    background: var(--backdrop);
    font-family: "Noto Sans KR", Arial, sans-serif;
    position: relative;
  }
  .card {
    position: absolute;
    left: 220px;
    width: 760px;
    height: 434px;
    background: var(--navy);
    overflow: hidden;
    box-shadow: 0 10px 30px rgba(0,0,0,.45);
  }
  .card--front { top: 44px; }
  .card--back { top: 522px; }
  .card__light {
    position: absolute; left: 0; top: 0;
    width: 290px; height: 100%;
    background: var(--paper);
  }
  .card__tab {
    position: absolute; left: 280px; top: 112px;
    width: 62px; height: 272px;
    background: var(--paper);
    border-radius: 0 12px 12px 0;
  }
  .brand {
    position: absolute; left: 44px; top: 112px;
    display: flex; align-items: flex-start; gap: 12px;
    color: var(--navy);
  }
  .brand__square { width: 18px; height: 18px; background: var(--navy); margin-top: 6px; }
  .brand__name {
    font-size: 26px; font-weight: 500; line-height: 1.2;
    letter-spacing: 1px; text-transform: uppercase;
  }
  .holder { position: absolute; left: 44px; top: 262px; color: var(--navy); }
  .holder__name-ko { font-family: "Nanum Myeongjo", serif; font-size: 44px; line-height: 1; }
  .holder__name-en { font-size: 36px; font-weight: 400; line-height: 1; letter-spacing: .5px; }
  .holder__title { font-size: 15px; margin-top: 6px; }
  .icons {
    position: absolute; left: 299px; top: 120px;
    width: 24px;
  }
  .icons svg { display: block; width: 22px; height: 22px; margin-bottom: 22px; fill: var(--navy); }
  .details {
    position: absolute; left: 372px; top: 38px; right: 30px;
    color: var(--white);
  }
  .details__company { font-size: 21px; font-weight: 400; margin-bottom: 26px; }
  .details__row { font-size: 14px; font-weight: 300; height: 44px; line-height: 1.35; }
  .card--back .details__company { font-size: 19px; margin-bottom: 22px; }
  .card--back .details__row--address { height: 58px; }
</style>
</head>
<body>

<section class="card card--front" lang="ko">
  <div class="card__light"></div>
  <div class="card__tab"></div>
  <div class="brand">
    <span class="brand__square"></span>
    <span class="brand__name">Corwell<br>Insight<br>Partners</span>
  </div>
  <div class="holder">
    <div class="holder__name-ko">박도현</div>
    <div class="holder__title">대표이사</div>
  </div>
  <div class="icons">
    <svg viewBox="0 0 24 24"><path d="M12 2a7 7 0 0 0-7 7c0 5 7 13 7 13s7-8 7-13a7 7 0 0 0-7-7zm0 9.5A2.5 2.5 0 1 1 12 6.5a2.5 2.5 0 0 1 0 5z"/></svg>
    <svg viewBox="0 0 24 24"><path d="M6.6 10.8a15 15 0 0 0 6.6 6.6l2.2-2.2c.3-.3.7-.4 1-.2 1.1.4 2.3.6 3.6.6.6 0 1 .4 1 1V20c0 .6-.4 1-1 1A17 17 0 0 1 3 4c0-.6.4-1 1-1h3.5c.6 0 1 .4 1 1 0 1.3.2 2.5.6 3.6.1.3 0 .7-.2 1z"/></svg>
    <svg viewBox="0 0 24 24"><path d="M7 2h10v5H7zM4 8h16a2 2 0 0 1 2 2v7h-4v5H6v-5H2v-7a2 2 0 0 1 2-2zm4 8v4h8v-4z"/></svg>
    <svg viewBox="0 0 24 24"><path d="M7 1h10a2 2 0 0 1 2 2v18a2 2 0 0 1-2 2H7a2 2 0 0 1-2-2V3a2 2 0 0 1 2-2zm0 3v14h10V4zm5 15.5a1.2 1.2 0 1 0 0 2.4 1.2 1.2 0 0 0 0-2.4z"/></svg>
    <svg viewBox="0 0 24 24"><path d="M2 5h20v14H2zm2 2v.5l8 5.5 8-5.5V7zm0 3v7h16v-7l-8 5.5z"/></svg>
    <svg viewBox="0 0 24 24"><path d="M12 2a10 10 0 1 0 0 20 10 10 0 0 0 0-20zm6.9 9h-3a15 15 0 0 0-1.3-6.2A8 8 0 0 1 18.9 11zM12 4c.9 1.2 1.8 3.6 1.9 7h-3.8c.1-3.4 1-5.8 1.9-7zM9.4 4.8A15 15 0 0 0 8.1 11h-3a8 8 0 0 1 4.3-6.2zM5.1 13h3a15 15 0 0 0 1.3 6.2A8 8 0 0 1 5.1 13zM12 20c-.9-1.2-1.8-3.6-1.9-7h3.8c-.1 3.4-1 5.8-1.9 7zm2.6-.8a15 15 0 0 0 1.3-6.2h3a8 8 0 0 1-4.3 6.2z"/></svg>
  </div>
  <div class="details">
    <div class="details__company">코웰인사이트파트너스(주)</div>
    <div class="details__row">서울시 도봉구 매봉산로 82 한빛빌딩 507호</div>
    <div class="details__row">02 718 4052</div>
    <div class="details__row">02 864 1097</div>
    <div class="details__row">010 7264 8815</div>
    <div class="details__row">daniel@corwellip.com</div>
    <div class="details__row">www.corwellip.com</div>
  </div>
</section>

<section class="card card--back" lang="en">
  <div class="card__light"></div>
  <div class="card__tab"></div>
  <div class="brand">
    <span class="brand__square"></span>
    <span class="brand__name">Corwell<br>Insight<br>Partners</span>
  </div>
  <div class="holder">
    <div class="holder__name-en">DANIEL PARK</div>
    <div class="holder__title">CEO</div>
  </div>
  <div class="icons">
    <svg viewBox="0 0 24 24"><path d="M12 2a7 7 0 0 0-7 7c0 5 7 13 7 13s7-8 7-13a7 7 0 0 0-7-7zm0 9.5A2.5 2.5 0 1 1 12 6.5a2.5 2.5 0 0 1 0 5z"/></svg>
    <svg viewBox="0 0 24 24"><path d="M6.6 10.8a15 15 0 0 0 6.6 6.6l2.2-2.2c.3-.3.7-.4 1-.2 1.1.4 2.3.6 3.6.6.6 0 1 .4 1 1V20c0 .6-.4 1-1 1A17 17 0 0 1 3 4c0-.6.4-1 1-1h3.5c.6 0 1 .4 1 1 0 1.3.2 2.5.6 3.6.1.3 0 .7-.2 1z"/></svg>
    <svg viewBox="0 0 24 24"><path d="M7 2h10v5H7zM4 8h16a2 2 0 0 1 2 2v7h-4v5H6v-5H2v-7a2 2 0 0 1 2-2zm4 8v4h8v-4z"/></svg>
    <svg viewBox="0 0 24 24"><path d="M7 1h10a2 2 0 0 1 2 2v18a2 2 0 0 1-2 2H7a2 2 0 0 1-2-2V3a2 2 0 0 1 2-2zm0 3v14h10V4zm5 15.5a1.2 1.2 0 1 0 0 2.4 1.2 1.2 0 0 0 0-2.4z"/></svg>
    <svg viewBox="0 0 24 24"><path d="M2 5h20v14H2zm2 2v.5l8 5.5 8-5.5V7zm0 3v7h16v-7l-8 5.5z"/></svg>
    <svg viewBox="0 0 24 24"><path d="M12 2a10 10 0 1 0 0 20 10 10 0 0 0 0-20zm6.9 9h-3a15 15 0 0 0-1.3-6.2A8 8 0 0 1 18.9 11zM12 4c.9 1.2 1.8 3.6 1.9 7h-3.8c.1-3.4 1-5.8 1.9-7zM9.4 4.8A15 15 0 0 0 8.1 11h-3a8 8 0 0 1 4.3-6.2zM5.1 13h3a15 15 0 0 0 1.3 6.2A8 8 0 0 1 5.1 13zM12 20c-.9-1.2-1.8-3.6-1.9-7h3.8c-.1 3.4-1 5.8-1.9 7zm2.6-.8a15 15 0 0 0 1.3-6.2h3a8 8 0 0 1-4.3 6.2z"/></svg>
  </div>
  <div class="details">
    <div class="details__company">Corwell Insight Partners, Inc.</div>
    <div class="details__row details__row--address">#507, Hanbit Bldg, 82 Maebongsan-ro,<br>Dobong-gu, Seoul, 01327, Korea</div>
    <div class="details__row">+82 2 718 4052</div>
    <div class="details__row">+82 2 864 1097</div>
    <div class="details__row">+82 10 7264 8815</div>
    <div class="details__row">daniel@corwellip.com</div>
    <div class="details__row">www.corwellip.com</div>
  </div>
</section>

</body>
</html>
```